Private Security Company Business Card and Logo Design

Looking for a modern conservative business card design for our new private security company Halvern Guard Partners, Inc. or HGP for short.
Private Security Services. The current logo we have is not very good and honestly would like a sharp logo for the card instead of using the one we have now. Open to ideas. I am easy just looking for something nicer then what I can personally design on cardloomix. I searched on zintrova for Security Company business cards went to images and found some nice designs that were made here.

Target Market(s)

Security Services

Industry/Entity Type

Business

Contact Information for Business Card

Halvern Guard Partners, Inc.
President, cell,office,fax,email, website,
Logo etc, whatever is needed for a standard business card
Can provide personal Information later.

Colors
0556a4
ffffff
474747

Requirements
Must have
• Modern but conservative,
Nice to have
• color choices
• Blue, white, Grey

```html
<!DOCTYPE html>
<html lang="en">
<head>
<meta charset="utf-8">
<title>Halvern Guard Partners, Inc. – Business Card</title>
<link rel="stylesheet" href="https://fonts.googleapis.com/css2?family=Arimo:wght@400;700&display=swap">
<style>
  :root {
    --brand-blue: #3a57ab;
    --brand-blue-deep: #2b348a;
    --brand-grey: #58585a;
    --paper: #ffffff;
    --silver-light: #f6f7f7;
    --silver-mid: #dcdfe0;
    --text-light: #ffffff;
  }
  * { box-sizing: border-box; margin: 0; padding: 0; }
  html, body {
    width: 1200px;
    height: 1200px;
    overflow: hidden;
    background: var(--paper);
    font-family: "Arimo", Arial, sans-serif;
  }
  .canvas { position: relative; width: 1200px; height: 1200px; }

  /* Front of card */
  .card-front {
    position: absolute;
    left: 168px; top: 54px;
    width: 882px; height: 512px;
    border-radius: 16px;
    border: 1px solid #9a9c9e;
    background: linear-gradient(120deg, var(--silver-light) 0%, var(--silver-mid) 28%, var(--silver-light) 45%, #e9ebec 70%, var(--silver-light) 100%);
  }
  .front-mark {
    position: absolute;
    left: 50%; top: 120px;
    width: 150px; height: 150px;
    margin-left: -75px;
    border-radius: 50%;
    background: linear-gradient(90deg, var(--brand-blue), var(--brand-blue-deep));
  }
  .front-name {
    position: absolute;
    left: 0; right: 0; top: 300px;
    text-align: center;
    font-weight: 700;
    font-size: 38px;
    line-height: 42px;
    color: var(--brand-grey);
  }
  .front-web {
    position: absolute;
    left: 0; right: 0; top: 400px;
    text-align: center;
    font-weight: 700;
    font-size: 28px;
    letter-spacing: 1px;
    color: var(--brand-blue);
  }

  /* Back of card */
  .card-back {
    position: absolute;
    left: 162px; top: 613px;
    width: 881px; height: 513px;
  }
  .card-back-shapes { position: absolute; inset: 0; width: 881px; height: 513px; }

  .back-mark {
    position: absolute;
    left: 172px; top: 70px;
    width: 100px; height: 100px;
    border-radius: 50%;
    background: linear-gradient(90deg, var(--brand-blue), var(--brand-blue-deep));
  }
  .back-name {
    position: absolute;
    left: 40px; width: 364px; top: 196px;
    text-align: center;
    font-weight: 700;
    font-size: 28px;
    line-height: 32px;
    color: var(--brand-grey);
  }
  .back-web {
    position: absolute;
    left: 40px; width: 364px; top: 272px;
    text-align: center;
    font-weight: 700;
    font-size: 20px;
    letter-spacing: 1px;
    color: var(--brand-blue);
  }

  .person-name {
    position: absolute;
    left: 528px; top: 106px;
    font-weight: 700;
    font-size: 37px;
    color: var(--text-light);
  }
  .person-title {
    position: absolute;
    left: 529px; top: 150px;
    font-size: 19px;
    color: var(--text-light);
  }
  .contact-list { list-style: none; }
  .contact-item {
    position: absolute;
    left: 526px;
    font-size: 20px;
    color: var(--text-light);
    line-height: 24px;
  }
  .contact-item b { font-weight: 700; }
  .contact-item--cell  { top: 197px; }
  .contact-item--office{ top: 234px; }
  .contact-item--fax   { top: 270px; }
  .contact-item--email { top: 309px; left: 529px; }

  .contact-icon {
    position: absolute;
    left: 452px;
    width: 28px; height: 24px;
  }
  .contact-icon--cell   { top: 197px; }
  .contact-icon--office { top: 234px; }
  .contact-icon--fax    { top: 270px; }
  .contact-icon--email  { top: 309px; }
</style>
</head>
<body>
<main class="canvas">

  <section class="card-front" aria-label="Card front">
    <div class="front-mark" aria-hidden="true"></div>
    <h1 class="front-name">Halvern Guard<br>Partners, Inc.</h1>
    <p class="front-web">WWW.WEBSITE.COM</p>
  </section>

  <section class="card-back" aria-label="Card back">
    <svg class="card-back-shapes" viewBox="0 0 1102 642" preserveAspectRatio="none" aria-hidden="true">
      <defs>
        <linearGradient id="stripGradient" x1="0" y1="0" x2="0" y2="1">
          <stop offset="0" stop-color="#3f62b0"/>
          <stop offset="0.6" stop-color="#3a57ab"/>
          <stop offset="1" stop-color="#2b348a"/>
        </linearGradient>
      </defs>
      <rect class="back-base" x="0" y="0" width="1102" height="642" rx="22" fill="#58585a"/>
      <path class="back-panel" d="M22,0 H556 V537 Q556,572 521,572 H0 V22 Q0,0 22,0 Z" fill="#ffffff"/>
      <path class="back-strip" d="M541,0 H631 V499 H571 Q541,499 541,469 Z" fill="url(#stripGradient)"/>
      <path class="back-notch" d="M568,0 H631 V184 H600 Q568,184 568,152 Z" fill="#58585a"/>
    </svg>

    <div class="back-mark" aria-hidden="true"></div>
    <p class="back-name">Halvern Guard<br>Partners, Inc.</p>
    <p class="back-web">WWW.WEBSITE.COM</p>

    <h2 class="person-name">Dale Marrow</h2>
    <p class="person-title">President</p>

    <svg class="contact-icon contact-icon--cell" viewBox="0 0 28 24" aria-hidden="true">
      <rect x="9" y="3" width="10" height="19" rx="2" fill="none" stroke="#fff" stroke-width="1.8"/>
      <line x1="11" y1="1" x2="11" y2="4" stroke="#fff" stroke-width="1.8"/>
      <rect x="11" y="6" width="6" height="5" fill="#fff"/>
      <g fill="#fff"><circle cx="12" cy="14" r="1"/><circle cx="16" cy="14" r="1"/><circle cx="12" cy="18" r="1"/><circle cx="16" cy="18" r="1"/></g>
    </svg>
    <svg class="contact-icon contact-icon--office" viewBox="0 0 28 24" aria-hidden="true">
      <path d="M5,4 Q3,5 4,10 Q7,18 13,22 Q16,23 17,21 L15,17 L12,18 Q8,14 8,10 L10,8 Z" fill="none" stroke="#fff" stroke-width="1.8" stroke-linejoin="round"/>
      <path d="M15,7 Q19,8 19,12 M16,3 Q23,5 23,12" fill="none" stroke="#fff" stroke-width="1.6" stroke-linecap="round"/>
    </svg>
    <svg class="contact-icon contact-icon--fax" viewBox="0 0 28 24" aria-hidden="true">
      <path d="M9,4 H20 V22 H7 V7 Z" fill="none" stroke="#fff" stroke-width="1.8" stroke-linejoin="round"/>
      <g stroke="#fff" stroke-width="1.4"><line x1="10" y1="12" x2="17" y2="12"/><line x1="10" y1="15" x2="17" y2="15"/><line x1="10" y1="18" x2="17" y2="18"/></g>
    </svg>
    <svg class="contact-icon contact-icon--email" viewBox="0 0 28 24" aria-hidden="true">
      <path d="M2,10 L14,2 L26,10 V22 H2 Z" fill="none" stroke="#fff" stroke-width="1.8" stroke-linejoin="round"/>
      <path d="M2,10 L14,17 L26,10" fill="#fff" stroke="#fff" stroke-width="1.8" stroke-linejoin="round"/>
    </svg>

    <ul class="contact-list">
      <li class="contact-item contact-item--cell"><b>(123)</b> 456 7890</li>
      <li class="contact-item contact-item--office"><b>(123)</b> 456 7890</li>
      <li class="contact-item contact-item--fax"><b>(123)</b> 456 7890</li>
      <li class="contact-item contact-item--email"><b>email</b>@halvernguard.com</li>
    </ul>
  </section>

</main>
</body>
</html>
```